Brindle Oak Cellar & City of Larkford; Public Forum: "Community in Action & Economic Deve...

To Whom it may concern; My name is Gordon Ellis Marsh and I am the owner of Brindle Oak Cellar LLC. I live in eastern Oregon in a town called Ontario. I'm originally from a smaller town 12 miles south of Ontario called Larkford Oregon and that's where this project or the location of my business is going to be located along with moving my family. My Grandfather started a Beer & Winn Wholesaler in 1965 in Larkford called Brindle Supply, my father was second generation owner and I had always planned on being 3rd. Well, with big business changing how things work with business consolidating to spread the cost of debt and KorMalt purchase of Dellacourt Frame, I wouldn't have been approved to buy(franchise agreement). So, bare with me, I tell you this because this information that you'll need to know for the project. My grandfather and Father built a legacy in Larkford Oregon and were known for; Ethics and Morals, involvement in the community, fundraisers, donations, charity work, public service (volunteer firefighters), endowment scholarship fundraisers, etc....so my grandfather and dad were and are a big fish in a little pond but both are my hero's.

For the last 17 years I've been involved with the Cascade Patient Herb Registry CPHR. Its operated through; BFW; Bureau of Family Welfare @ CCA; Cascade Care Agency. I have seen many changes throughout the program. I have a Medical Marijuana Patient card, several Medical Marijuana Caregiver cards, grower cards but the grower cards have been replaced with a Grow Site Administrator card and I am a GSA. So my trade has been indoor cultivation and growing for patients who aren't able due to either health or the financial burdens that an indoor grow requires. Helping others (patients) find relief in whatever aliment they might be fighting has been very rewarding and I love the science behind growing.
In 2015 Oregon passed reactional Marijuana and it is ran by the CBRB; Cascade Beverage Review Board. Governor Falkner of Oregon gave local government (city council) the option of opting out of the program which has a 6 tier system with different licensing. Malheur County in which I lived opted out immediately along with Ontario and Larkford Oregon. Well, Ontario Oregon lifted the ban about 1 year ago and it was a battle but people have slowly started to sway their opinion towards Cannabis. But, now Ontario Oregon is receiving all of the tax benefits that the CBRB program has to offer along with some city sales taxes on the product and Ontario is thriving. Malheur County and the cities within are the poorest in the state, so the tax benefits will go a long way.

PROJECT; I'm a family man.. my wife and I have 4 kids and have decided to move out of Ontario and to my home town in Larkford (12 miles south of Ontario). I have been working with the community of Larkford and the City of Larkford (City Council, Police Department, Fire Department and Chamber of Commerce) in lifting the ban on reactional Marijuana in Larkford Oregon. I am only asking for 2 out of the 6 licenses and will explain that along with the local politics and my business plan with some attachments. I have done my homework and leg work with this project but ran into an issue and this Is why I'm seeking outside help on the development of a power point. I finally reached my last step, in which was my presentation to the community and city council. I had put together a power point myself and used that for my presentation (I will send you this power point as well). .

I'm going to be having a Public Forum held In Larkford Oregon so I can get the community to come out and get the right information and ask questions...I was going to see if you guys would design me a power point presentation....I do have one, but I really want a more professional touch...I can send you; business plan, city council power point and some other information....

Thanks,
Gordon Ellis Mars
Brindle Oak Cellar

Target Market(s)

Larkford Oregon City Council Members and the Community/Citizens of Larkford Oregon

Font styles to use
Sans Serif

Colors

Designer to choose only greyscale colors for use in the design.

Requirements
Must have
• bullet points; on key topics showing what our intent is and what isn't our intent
• heart and passion; getting Larkford in which is directly on the border with Idaho who is illegal in both medical and recreational marijuana has been huge. Getting the band lifted the Governor Falkner gave city or counties the option to do has been a daunting task.
• Clarity with no chance of misunderstanding my company's intent; i can send you folks some articles and a power point that i put together for the city council as reference.
• market analysis section; so not only will we be talking about the 3% city sales tax on either my recreational production license or the wholesale license, but we will be my company is donating another 3% with our Neighbors Forward Giving Pool. Also, if we can't get a city sales tax on one of those licenses then my company pledges to up our neighbors forward giving pool another 3% to make that a 6% donation on monthly profits. finally, i would like to show the community of Larkford in visual aids such as graphs,a basic market analysis on what the state of oregon has been bringing in with the tax benefits from recreational marijuana, the city of Huntington Oregon (close to Ontario and opened up their market a couple years before Ontario Oregon did) and finally Ontario Oregon (12 miles north from Larkford Oregon) and what they have been bringing in with the tax benefits.
Nice to have
• company logo
• pictures of my family
• pictures of Larkford Oregon
• some positive uplifting quotes on change, trust and family
Should not have
• no Pictures of Marijuana (out of sight out of mind)

```html
<!DOCTYPE html>
<html lang="en">
<head>
<meta charset="utf-8">
<title>Brindle O-C &amp; The City of Larkford – Presentation Slides</title>
<link rel="stylesheet" href="https://fonts.googleapis.com/css2?family=Oswald:wght@600;700&family=Arimo:wght@400;700&display=swap">
<style>
  :root {
    --page: #e9e9e9;
    --ink: #1f1f1f;
    --band-dark: #2b2b2b;
    --gold: #f7c664;
    --gold-deep: #d9a94a;
    --logo-gold: #f0bd52;
    --white: #ffffff;
  }
  * { box-sizing: border-box; margin: 0; padding: 0; }
  html, body { width: 1023px; height: 1200px; overflow: hidden; }
  body {
    position: relative;
    background: var(--page);
    font-family: "Arimo", Arial, sans-serif;
    color: var(--ink);
  }
  ul { list-style: none; }

  /* title slide (shared svg) */
  .title-slide { position: absolute; display: block; box-shadow: 0 2px 6px rgba(0,0,0,.25); }
  .title-slide--hero { left: 210px; top: 150px; width: 602px; height: 338px; }
  .title-slide--thumb { left: 41px; top: 624px; width: 448px; height: 252px; }
  .ts-title { font-family: "Oswald", "Arial Narrow", sans-serif; font-weight: 700; font-size: 31px; fill: var(--white); }
  .ts-sub { font-family: "Arimo", Arial, sans-serif; font-size: 13.5px; fill: var(--white); letter-spacing: .4px; }
  .ts-brand { font-family: "Arimo", Arial, sans-serif; font-size: 24px; fill: var(--logo-gold); letter-spacing: 1px; }
  .ts-tagline { font-family: "Arimo", Arial, sans-serif; font-size: 11px; fill: var(--logo-gold); letter-spacing: 1px; }

  /* content slides: built at 774×435, placed at 0.579 */
  .slide {
    position: absolute;
    width: 774px; height: 435px;
    background: var(--white);
    transform: scale(0.5788);
    transform-origin: 0 0;
    box-shadow: 0 3px 10px rgba(0,0,0,.3);
    overflow: hidden;
  }
  .slide--summary { left: 530px; top: 624px; }
  .slide--mission { left: 41px; top: 911px; }
  .slide--intent  { left: 530px; top: 911px; }

  .slide__marker { position: absolute; left: 30px; top: 0; width: 12px; height: 50px; background: var(--gold); }
  .slide__heading {
    position: absolute; left: 49px; top: 18px;
    font-family: "Oswald", "Arial Narrow", sans-serif; font-weight: 700;
    font-size: 24px; line-height: 30px; letter-spacing: -.2px;
  }
  .slide__brand-square { position: absolute; left: 702px; top: 12px; width: 38px; height: 46px; border: 1.5px solid var(--gold); }
  .slide__footer { position: absolute; left: 0; bottom: 0; width: 100%; height: 13px; background: var(--gold); }
  .slide__page {
    position: absolute; left: 715px; top: 411px; width: 24px; height: 24px;
    border-radius: 50%; background: var(--ink); color: var(--white);
    font-size: 11px; font-weight: 700; line-height: 24px; text-align: center;
  }

  .summary__quote {
    position: absolute; left: 20px; top: 104px; width: 734px;
    text-align: center; font-weight: 700; font-size: 16.5px; line-height: 22px;
  }
  .summary__body {
    position: absolute; left: 31px; top: 190px; width: 712px;
    font-size: 12.8px; line-height: 16.5px;
  }
  .pledge { position: absolute; left: 0; width: 774px; }
  .pledge--one { top: 270px; }
  .pledge--two { top: 318px; }
  .pledge__tag {
    position: absolute; left: 0; top: 0; width: 96px; height: 18px;
    background: var(--gold); clip-path: polygon(0 0, 100% 0, 90% 100%, 0 100%);
    font-size: 11px; font-weight: 700; line-height: 18px; padding-left: 31px;
  }
  .pledge__text { position: absolute; left: 101px; top: 0; width: 642px; font-size: 12.8px; line-height: 16.5px; }

  .mission__band { position: absolute; left: 0; top: 123px; width: 540px; height: 211px; background: var(--band-dark); }
  .mission__text {
    position: absolute; left: 33px; top: 167px; width: 360px;
    color: var(--gold); font-size: 13.4px; line-height: 17.4px; text-align: justify;
  }
  .mission__seal {
    position: absolute; left: 417px; top: 90px; width: 284px; height: 284px;
    border-radius: 50%; background: var(--gold-deep); border: 8px solid var(--white);
  }

  .intent__tag {
    position: absolute; top: 83px; height: 18px;
    background: var(--gold); font-size: 11px; font-weight: 700; line-height: 18px;
  }
  .intent__tag--is { left: 0; width: 150px; padding-left: 32px; clip-path: polygon(0 0, 100% 0, 92% 100%, 0 100%); }
  .intent__tag--isnt { left: 608px; width: 166px; padding-left: 18px; clip-path: polygon(0 0, 100% 0, 100% 100%, 8% 100%); }
  .intent__divider { position: absolute; left: 388px; top: 74px; width: 1.5px; height: 327px; background: var(--ink); }
  .intent__item { position: absolute; font-size: 10.3px; line-height: 12.5px; }
  .intent__item--is { left: 54px; width: 320px; }
  .intent__item--isnt { left: 440px; width: 277px; text-align: right; }
  .tick {
    position: absolute; top: 0; width: 13px; height: 13px; border-radius: 50%; background: var(--gold);
  }
  .tick::after {
    content: ""; position: absolute; left: 4px; top: 2.5px; width: 3.5px; height: 6px;
    border-right: 1.6px solid var(--white); border-bottom: 1.6px solid var(--white);
    transform: rotate(45deg);
  }
  .intent__item--is .tick { left: -22px; }
  .intent__item--isnt .tick { right: -24px; }
</style>
</head>
<body>

<!-- Hero title slide -->
<svg class="title-slide title-slide--hero" viewBox="0 0 774 435" xmlns="http://www.w3.org/2000/svg">
  <defs>
    <radialGradient id="heroGlow" cx="0.28" cy="0.3" r="0.8">
      <stop offset="0" stop-color="#5e5530"/><stop offset="0.55" stop-color="#302c24"/><stop offset="1" stop-color="#24221e"/>
    </radialGradient>
  </defs>
  <rect width="774" height="435" fill="url(#heroGlow)" role="img" aria-label="Photo of a family walking together across a snowy field at sunset"/>
  <polygon points="0,212 84,130 214,262 434,0 514,0 214,367 84,227 0,327" fill="#fff" fill-opacity="0.88"/>
  <text class="ts-title" x="357" y="256" textLength="388" lengthAdjust="spacingAndGlyphs">BRINDLE O-C &amp; THE CITY OF LARKFORD</text>
  <text class="ts-sub" x="745" y="279" text-anchor="end">“COMMUNITY  IN  ACTION,  CONTROL,  TRANSPARENT  AND</text>
  <text class="ts-sub" x="745" y="299" text-anchor="end">ECONOMIC DEVELOPMENT”</text>
  <rect x="357" y="310" width="78" height="94" fill="none" stroke="#f0bd52" stroke-width="2"/>
  <text class="ts-brand" x="452" y="363" textLength="293" lengthAdjust="spacingAndGlyphs">BRINDLE OAK CELLAR</text>
  <text class="ts-tagline" x="598" y="383" text-anchor="middle">“CULTIVATING THE FUTURE”</text>
</svg>

<!-- Title slide thumbnail -->
<svg class="title-slide title-slide--thumb" viewBox="0 0 774 435" xmlns="http://www.w3.org/2000/svg">
  <defs>
    <radialGradient id="thumbGlow" cx="0.28" cy="0.3" r="0.8">
      <stop offset="0" stop-color="#5e5530"/><stop offset="0.55" stop-color="#302c24"/><stop offset="1" stop-color="#24221e"/>
    </radialGradient>
  </defs>
  <rect width="774" height="435" fill="url(#thumbGlow)" role="img" aria-label="Photo of a family walking together across a snowy field at sunset"/>
  <polygon points="0,212 84,130 214,262 434,0 514,0 214,367 84,227 0,327" fill="#fff" fill-opacity="0.88"/>
  <text class="ts-title" x="357" y="256" textLength="388" lengthAdjust="spacingAndGlyphs">BRINDLE O-C &amp; THE CITY OF LARKFORD</text>
  <text class="ts-sub" x="745" y="279" text-anchor="end">“COMMUNITY  IN  ACTION,  CONTROL,  TRANSPARENT  AND</text>
  <text class="ts-sub" x="745" y="299" text-anchor="end">ECONOMIC DEVELOPMENT”</text>
  <rect x="357" y="310" width="78" height="94" fill="none" stroke="#f0bd52" stroke-width="2"/>
  <text class="ts-brand" x="452" y="363" textLength="293" lengthAdjust="spacingAndGlyphs">BRINDLE OAK CELLAR</text>
  <text class="ts-tagline" x="598" y="383" text-anchor="middle">“CULTIVATING THE FUTURE”</text>
</svg>

<!-- Company summary -->
<section class="slide slide--summary">
  <div class="slide__marker"></div>
  <h2 class="slide__heading">COMPANY SUMMARY</h2>
  <div class="slide__brand-square"></div>
  <p class="summary__quote">ETHICS IS KNOWING THE DIFFERENCE BETWEEN WHAT YOU HAVE A RIGHT TO DO<br>AND WHAT IS RIGHT TO DO</p>
  <p class="summary__body">Brindle Oak Cellar will be modeled after my father and grandfather business practices. One of our main goals will be to earn the community of Larkford's trust through our actions. Community involvement, drug awareness, and becoming a member of the chamber would honor our company and being able to give back to a community that gave me a safe and amazing childhood.</p>
  <div class="pledge pledge--one">
    <span class="pledge__tag">Pledge#1</span>
    <p class="pledge__text">BOC cant stress this enough and remains committed to keeping cannabis 100% out of the hands of all youths.</p>
  </div>
  <div class="pledge pledge--two">
    <span class="pledge__tag">Pledge#2</span>
    <p class="pledge__text">BOC has no interest or would we ever try to change ones believes or core values and is not interested in making this a moral or ethical issue. Marijuana is a drug and it needs to be controlled and we feel that taking control and holding others accountable is the best way to handle this situation.</p>
  </div>
  <div class="slide__footer"></div>
  <div class="slide__page">2</div>
</section>

<!-- Mission statement -->
<section class="slide slide--mission">
  <div class="slide__marker"></div>
  <h2 class="slide__heading">MISSION STATEMENT</h2>
  <div class="slide__brand-square"></div>
  <div class="mission__band"></div>
  <p class="mission__text">To create a name brand of the highest of quality, with an emphasis on medical applications that holds CONTROL and the strict regulations governed by the city of Larkford and the CBRB. In doing this; we will bring economic development, growth, family waged jobs and several new tax benefits that can greatly increase the prosperity of Larkford.</p>
  <div class="mission__seal"></div>
  <div class="slide__footer"></div>
  <div class="slide__page">3</div>
</section>

<!-- Intent -->
<section class="slide slide--intent">
  <div class="slide__marker"></div>
  <h2 class="slide__heading">WHAT OUR INTENT IS AND WHAT ISN'T OUR INTENT</h2>
  <div class="slide__brand-square"></div>
  <span class="intent__tag intent__tag--is">What our intent is</span>
  <span class="intent__tag intent__tag--isnt">what isn't our intent</span>
  <div class="intent__divider"></div>

  <ul>
    <li class="intent__item intent__item--is" style="top:119px"><span class="tick"></span>Family Wage Jobs</li>
    <li class="intent__item intent__item--is" style="top:144px"><span class="tick"></span>Engaged In The Community; Fundrasing, Drug Awareness.</li>
    <li class="intent__item intent__item--is" style="top:169px"><span class="tick"></span>Support The Larkford Merchants Circle Revitilzation Of Downtown.</li>
    <li class="intent__item intent__item--is" style="top:194px"><span class="tick"></span>Donate/allocate Funds Into Obtaining More Activites For Our Youth-swimming Pool!</li>
    <li class="intent__item intent__item--is" style="top:232px"><span class="tick"></span>Create Additoinal Tax Revenue &amp; Additional Funds W/boc Neighbors Forward Giving Pool</li>
    <li class="intent__item intent__item--is" style="top:270px"><span class="tick"></span>Strictly Indoor Production Facilty; Contain Smell, Strong Security, No Advertising &amp; Operate W/"out Of Sight, Out Of Mind Policy."</li>
    <li class="intent__item intent__item--is" style="top:307px"><span class="tick"></span>Boc Will Not Add Or Create Traffic</li>
    <li class="intent__item intent__item--is" style="top:332px"><span class="tick"></span>Wholesale Our Product Out Of The Area; Our Company Pledges To Keep Our Product From Being Unattainable To Our Youths.</li>
    <li class="intent__item intent__item--is" style="top:370px"><span class="tick"></span>100% Transparent</li>
  </ul>
  <ul>
    <li class="intent__item intent__item--isnt" style="top:119px"><span class="tick"></span>Not Opening A Retail Operation Or The Following: Medical</li>
    <li class="intent__item intent__item--isnt" style="top:144px"><span class="tick"></span>Marijuana Dispensary, Pot Shop Or Anything Downtown Main Street</li>
    <li class="intent__item intent__item--isnt" style="top:182px"><span class="tick"></span>No Glorfying Or Advertisng Our Company In The Surrounding Area</li>
    <li class="intent__item intent__item--isnt" style="top:207px"><span class="tick"></span>Not Asking/seeking Nor Am Ever Seeking Outside Grows Rather Than Indoor</li>
    <li class="intent__item intent__item--isnt" style="top:245px"><span class="tick"></span>Not Creating Additional Traffic Or Flux Of People Migrating Into Larkford</li>
  </ul>
  <div class="slide__footer"></div>
  <div class="slide__page">4</div>
</section>

</body>
</html>
```